Scuba diving website (Only 1 page. If nice all website later for you)

The payment is for one page only. We are looking for the main design of our new website. For test you will have to redesign the page that is attached to this description. If we like the style we will choose you as the main designer for the whole website (around 20 pages).
The website is about scuba diving. It targets world wide in 4 languages dive centers, divers, underwater photographers, dive sites research, fish species info many more to come. The website is bulid on strong fondation and expect high visits. Developpment is done.
We need now to find the perfect design. The page to redesign is a page about a "dive center" that subscribe to the website where he presents himself and fills it's information. (like a facebook page).
We are looking for between MODERN and MINIMAL design, but most of all a CLEAN design. See below some design website we like
http://velorant.com/loft/
http://www.quennaby.com/
http://www.trevashun.com/
http://widgets.pelmaroskel.com/
For the color stay around the blue and orange. The page width should be 1024px.
Updates
You can use small diving pictures for presenting the "Neighbouring dive sites" in the page. (instead of the red and white flag)
Target Market(s)
We target people willing to go on holiday for diving. We target photographer, cameraman who wants to share picture of their dive, we target people who have an interest for fish species (they can tag more than 32000 different species on their picture/video). We target dive centers who want to advertise on the website by creating their own page

```html
<!DOCTYPE html>
<html lang="en">
<head>
<meta charset="utf-8">
<title>Scuba diving Center</title>
<link rel="stylesheet" href="https://fonts.googleapis.com/css2?family=Ubuntu:wght@300;400;500&family=Arimo:wght@400;700&family=Lora:wght@700&display=swap">
<style>
:root{
  --orange:#f39a2b;
  --orange-deep:#f07f0c;
  --orange-text:#ee8418;
  --blue:#2b7bbd;
  --blue-btn:#2f7fd0;
  --page:#eeeeee;
  --card:#ffffff;
  --text:#333333;
  --muted:#777777;
  --line:#d6d6d6;
  --dark:#2b2b2b;
  --darker:#232323;
  --foot-text:#bdbdbd;
  --red:#d8361e;
  --water-a:#1b5f9a;
  --water-b:#0c3560;
}
*{box-sizing:border-box;margin:0;padding:0}
html,body{width:1200px;height:2182px;overflow:hidden}
body{position:relative;background:var(--page);font-family:"Arimo",Arial,sans-serif;color:var(--text)}
.abs{position:absolute}
.site-header{position:absolute;left:0;top:0;width:1200px;height:73px;background:var(--orange);box-shadow:0 2px 4px rgba(0,0,0,.2)}
.brand{position:absolute;left:87px;top:19px;font-family:"Ubuntu",sans-serif;font-weight:500;font-size:28px;color:#fff}
.nav a{position:absolute;top:40px;font-size:14px;color:#fff;text-decoration:none;transform:translateX(-50%)}
.nav .home{top:29px;left:572px;width:84px;height:38px;transform:none;background:#444;border-radius:3px;text-align:center;line-height:38px}
.flag{position:absolute;top:8px;width:20px;height:14px}
.top-white{position:absolute;left:0;top:73px;width:1200px;height:20px;background:#f6f6f6}
.hero{left:89px;top:93px;width:1025px;height:412px;background:#fff}
.hero-photo{left:106px;top:110px;width:992px;height:379px;background:linear-gradient(180deg,#2a86c8 0%,#175c98 55%,#0f4570 100%)}
.search-frame{left:403px;top:346px;width:470px;height:119px;background:#d9d9d9;border-radius:14px;box-shadow:0 2px 6px rgba(0,0,0,.35)}
.search-box{left:422px;top:360px;width:433px;height:91px;background:linear-gradient(#f6a03a,var(--orange-deep));border-radius:9px}
.search-title{left:432px;top:370px;font-family:"Ubuntu",sans-serif;font-size:22px;color:#fff}
.search-input{left:430px;top:404px;width:280px;height:28px;background:#fff;border:1px solid #ccc;border-radius:3px;font-size:12px;color:#999;padding:7px 6px}
.search-btn{left:731px;top:401px;width:99px;height:31px;background:linear-gradient(#4c9be6,var(--blue-btn));border-radius:4px;color:#fff;font-family:"Ubuntu",sans-serif;font-size:19px;text-align:center;line-height:31px}
.h-sec{position:absolute;font-family:"Ubuntu",sans-serif;font-weight:400;color:var(--blue);font-size:20px;border-bottom:1px solid var(--line);padding-bottom:4px}
.h-sec b{font-weight:400;color:var(--orange-text);font-size:27px}
.h-sec.about{color:var(--orange-text)}
.h-sec.about b{color:var(--blue)}
.about-text{left:89px;top:571px;width:1025px;font-size:13px;line-height:20px;color:#333}
.read-more{left:93px;top:670px;font-size:13px;color:#b4530a;font-weight:700}
.card{position:absolute;background:var(--card);box-shadow:0 1px 3px rgba(0,0,0,.12)}
.ph{position:absolute}
.team-photo{left:11px;top:2px;width:194px;height:112px}
.team-text{position:absolute;left:11px;top:128px;width:194px;font-size:12px;line-height:15px;color:#333;text-align:justify}
.team-text .lead{color:var(--orange-text)}
.team-foot{position:absolute;left:11px;right:11px;font-size:12px;color:#777;border-top:1px solid #e2e2e2;padding-top:12px;display:flex;justify-content:space-between}
.btn-dark{position:absolute;height:37px;background:#111;border-radius:4px;color:var(--orange-text);font-family:"Ubuntu",sans-serif;font-size:15px;text-align:center;line-height:37px;box-shadow:0 2px 3px rgba(0,0,0,.4)}
.pager{position:absolute;display:flex;gap:4px;font-size:11px}
.pager span{height:20px;min-width:18px;line-height:20px;text-align:center;border:1px solid #ddd;background:#fafafa;color:#999;padding:0 4px}
.pager .on{background:#111;color:#fff;border-color:#111}
.thumb-box{position:absolute;top:1117px;width:144px;height:136px;background:#fff;box-shadow:0 1px 3px rgba(0,0,0,.12)}
.thumb-box .ph{left:9px;top:9px;width:126px;height:118px}
.gal-small{position:absolute;top:1004px;width:80px;height:81px;border:1px solid #ddd;background:#fff;padding:3px}
.gal-small div{width:100%;height:100%}
.gal-cap{position:absolute;left:859px;top:1096px;font-size:12px;line-height:17px}
.gal-meta{position:absolute;left:855px;top:1153px;width:245px;font-size:10px;color:#999;display:flex;justify-content:space-between;border-top:1px solid #eee;padding-top:10px}
.video-banner{left:839px;top:1190px;width:269px;height:61px;background:linear-gradient(#3b8fd2,#1e5fa8)}
.video-banner .lbl{position:absolute;left:6px;top:28px;background:#fff;color:#1d4f96;font-weight:700;font-size:12px;padding:2px 4px;text-decoration:underline}
.video-banner .chk{position:absolute;left:180px;top:14px;width:80px;height:37px;border:2px solid #fff;border-radius:4px;background:#5aa3df;color:#fff;font-size:15px;font-weight:700;text-align:center;line-height:14px;padding-top:4px}
.video-banner .chk small{font-size:9px;font-weight:400}
.neigh-band{left:89px;top:1368px;width:1024px;height:12px;background:linear-gradient(#e3e3e3,var(--page))}
.site{position:absolute;top:1488px;width:224px;height:192px;background:#e6e6e6;border-bottom:3px solid var(--red);box-shadow:0 1px 2px rgba(0,0,0,.15)}
.site .av{position:absolute;left:62px;top:-46px;width:94px;height:94px;border-radius:50%;border:3px solid var(--red);background:#fff;padding:5px}
.site .av div{width:100%;height:100%;border-radius:50%;background:radial-gradient(circle at 50% 40%,#4aa3d6,var(--water-b))}
.site h3{position:absolute;left:23px;top:54px;font-family:"Arimo",sans-serif;font-weight:400;font-size:19px;color:#2a8ac4}
.site ul{position:absolute;left:23px;top:84px;list-style:none;font-size:14px;line-height:20px;color:#333}
.stars{letter-spacing:1px;font-size:10px;color:#e8b423}
.stars.off{color:#c9c9c9}
.footer{left:0;top:1713px;width:1200px;height:406px;background:var(--dark)}
.footer-bar{left:0;top:2119px;width:1200px;height:63px;background:var(--darker)}
.f-h{position:absolute;top:1772px;font-family:"Lora",serif;font-weight:700;font-size:11px;color:#fff}
.f-txt{font-size:12px;line-height:22px;color:var(--foot-text)}
.post{position:absolute;left:346px;width:235px}
.post .th{position:absolute;left:0;top:0;width:62px;height:60px;background:linear-gradient(135deg,#1f7a6a,#2f9fb2)}
.post .t{position:absolute;left:76px;top:0;font-size:12px;color:#e6e6e6}
.post .x{position:absolute;left:76px;top:20px;width:165px;font-size:11px;line-height:19px;color:#8d8d8d}
.tags{position:absolute;left:608px;top:1818px;width:222px;display:flex;flex-wrap:wrap;gap:8px 5px}
.tags span{font-size:10px;color:#ccc;border:1px solid #555;background:#3a3a3a;padding:6px 6px;border-radius:2px}
.recent{position:absolute;left:870px;width:240px;border-bottom:1px solid #444;padding-bottom:10px}
.recent .t{font-size:12px;color:#e6e6e6}
.recent .d{font-size:10px;color:#8d8d8d;margin-top:5px}
.copy{left:89px;top:2136px;font-size:12px;color:#bbb}
.social{position:absolute;top:2143px;display:flex;gap:4px;left:868px}
.social span{width:20px;height:20px;display:block}
</style>
</head>
<body>

<header class="site-header">
  <div class="brand">Scuba diving Center</div>
  <nav class="nav">
    <a class="home" href="#">Home</a>
    <a href="#" style="left:710px">Latest</a>
    <a href="#" style="left:796px">Photos</a>
    <a href="#" style="left:879px">Vedios</a>
    <a href="#" style="left:947px">Fauna</a>
    <a href="#" style="left:1018px">Divers</a>
    <a href="#" style="left:1085px">Contact</a>
  </nav>
  <svg class="flag" style="left:978px" viewBox="0 0 20 14" role="img" aria-label="English"><rect width="20" height="14" fill="#23397a"/><path d="M0 0L20 14M20 0L0 14" stroke="#fff" stroke-width="3"/><path d="M0 0L20 14M20 0L0 14" stroke="#c8102e" stroke-width="1"/><path d="M10 0V14M0 7H20" stroke="#fff" stroke-width="4"/><path d="M10 0V14M0 7H20" stroke="#c8102e" stroke-width="2"/></svg>
  <svg class="flag" style="left:1035px" viewBox="0 0 20 14" role="img" aria-label="Deutsch"><rect width="20" height="5" fill="#000"/><rect y="5" width="20" height="4" fill="#dd0000"/><rect y="9" width="20" height="5" fill="#ffce00"/></svg>
  <svg class="flag" style="left:1091px" viewBox="0 0 20 14" role="img" aria-label="Español"><rect width="20" height="14" fill="#c60b1e"/><rect y="3.5" width="20" height="7" fill="#ffc400"/></svg>
</header>
<div class="top-white"></div>

<div class="abs hero"></div>
<div class="abs hero-photo" role="img" aria-label="Two divers swimming over a coral reef"></div>
<div class="abs search-frame"></div>
<div class="abs search-box"></div>
<div class="abs search-title">Find the best scuba drive</div>
<div class="abs search-input">enter your location here</div>
<div class="abs search-btn">Search</div>

<h2 class="h-sec about" style="left:89px;top:526px"><b>About</b> Scuba diving Center</h2>
<p class="abs about-text">Ipsum is simply dummy text of the printing and typesetting industry. Lorem Ipsum has been the industry's standard dummy text ever since the 1500s, when an unknown printer took a galley of type and scrambled it to make a type specimen book. It has survived not only five centuries, but also the leap into electronic typesetting, remaining essentially unchanged.<br>ummy text ever since the 1500s, when an unknown printer took a galley of type and scrambled it to make a type specimen book. It has survived not only five centuries, but also the leap into electronic typesetting, remaining essentially unchanged.</p>
<a class="abs read-more">Read More</a>

<h2 class="h-sec" style="left:87px;top:716px;width:217px"><b>The</b> Team</h2>
<article class="card" style="left:89px;top:764px;width:216px;height:237px">
  <div class="ph team-photo" style="background:linear-gradient(135deg,#c9b79b,#6e8fa6)" role="img" aria-label="Dive master on a boat deck"></div>
  <p class="team-text"><span class="lead">Ipsum is simply dummy text</span><br>of the printing and typesetting industry.Ipsum is simply<br>More Info</p>
  <div class="team-foot" style="top:200px"><span>Nice</span><span>Dive Master</span></div>
</article>
<article class="card" style="left:89px;top:1012px;width:216px;height:242px">
  <div class="ph team-photo" style="top:8px;background:linear-gradient(135deg,#3a8fbf,#b07a55)" role="img" aria-label="Instructor wearing a dive mask"></div>
  <p class="team-text" style="top:146px"><span class="lead">Ipsum is simply dummy text</span><br>of the printing and typesetting industry.Ipsum is simply<br>More Info</p>
  <div class="team-foot" style="top:211px"><span>ouin ouin</span><span>Instructor</span></div>
</article>
<div class="btn-dark" style="left:89px;top:1284px;width:97px">View All</div>

<h2 class="h-sec" style="left:336px;top:716px;width:477px"><b>Play</b> Slideshow</h2>
<div class="pager" style="left:717px;top:726px"><span class="on">1</span><span>2</span><span>Next ›</span></div>
<div class="card" style="left:336px;top:759px;width:477px;height:344px"></div>
<div class="ph" style="left:362px;top:780px;width:429px;height:298px;background:linear-gradient(180deg,#8fb4d8 0%,#c9d8e6 45%,#1f4f86 70%,#153b69 100%)" role="img" aria-label="Divers jumping from a dive boat"></div>
<div class="thumb-box" style="left:336px"><div class="ph" style="background:linear-gradient(135deg,#1e74c4,#e0782a)" role="img" aria-label="Reef fish over coral"></div></div>
<div class="thumb-box" style="left:502px"><div class="ph" style="background:linear-gradient(135deg,#4aa8e0,#1b5a96)" role="img" aria-label="Diver with mask close up"></div></div>
<div class="thumb-box" style="left:666px"><div class="ph" style="background:linear-gradient(135deg,#2a8fd0,#b8843e)" role="img" aria-label="Diver beside a coral head"></div></div>
<div class="btn-dark" style="left:336px;top:1279px;width:97px">View All</div>

<h2 class="h-sec" style="left:839px;top:716px;width:265px"><b>Scuba</b> Photogalley</h2>
<div class="card" style="left:839px;top:767px;width:274px;height:423px"></div>
<div class="ph" style="left:854px;top:787px;width:246px;height:201px;background:linear-gradient(90deg,#2a9fcf 0%,#3a7a5a 50%,#e69320 100%)" role="img" aria-label="Two discus fish facing each other"></div>
<div class="gal-small" style="left:850px"><div style="background:linear-gradient(135deg,#1c4f95,#2e86c8)" role="img" aria-label="Blue underwater scene"></div></div>
<div class="gal-small" style="left:935px"><div style="background:linear-gradient(135deg,#2b3f58,#c2732f)" role="img" aria-label="Fish among coral"></div></div>
<div class="gal-small" style="left:1020px"><div style="background:linear-gradient(135deg,#4a2e24,#c24a2a)" role="img" aria-label="Red reef creature"></div></div>
<p class="gal-cap"><span style="color:var(--orange-text)">Ipsum is simply dummy text</span><br>of the printing and typesetting</p>
<div class="gal-meta"><span>1 month ago</span><span>♥ 37 &nbsp;● 0</span></div>
<div class="abs video-banner" role="img" aria-label="Video gallery banner with underwater background"><span class="lbl">Scuba diving Vedio Gallery</span><span class="chk">CHECK<br><small>THEM OUT</small></span></div>
<div class="btn-dark" style="left:1012px;top:1279px;width:96px">View All</div>

<div class="abs neigh-band"></div>
<h2 class="h-sec" style="left:88px;top:1375px;border:0"><b style="font-size:22px">Neighbouring</b> dive sites</h2>
<div class="pager" style="left:1001px;top:1381px"><span class="on">1</span><span>2</span><span>Next ›</span></div>

<div class="site" style="left:89px"><div class="av"><div role="img" aria-label="Diver portrait"></div></div><h3>Nusa Penida</h3>
<ul><li>Rating: <span class="stars">★★★★★</span> (1 vote)</li><li>Distance 19.88 km</li><li>Comments: 0</li><li>photo: 0</li><li>video: 2</li></ul></div>
<div class="site" style="left:347px"><div class="av"><div role="img" aria-label="Diver portrait"></div></div><h3>Blue Lagoon</h3>
<ul><li>Rating: <span class="stars">★★★★★</span> (4 votes)</li><li>Distance 31.95 km</li><li>Comments: 3</li><li>photo: 84</li><li>video: 18</li></ul></div>
<div class="site" style="left:606px"><div class="av"><div role="img" aria-label="Diver portrait"></div></div><h3>White sand beach</h3>
<ul><li>Rating: <span class="stars off">★★★★★</span> (0 vote)</li><li>Distance 32.14 km</li><li>Comments: 0</li><li>photo: 7</li><li>video: 2</li></ul></div>
<div class="site" style="left:865px"><div class="av"><div role="img" aria-label="Diver portrait"></div></div><h3>Channel</h3>
<ul><li>Rating: <span class="stars off">★★★★★</span> (0 vote)</li><li>Distance 32.53 km</li><li>Comments: 0</li><li>photo: 8</li><li>video: 2</li></ul></div>

<footer class="abs footer"></footer>
<div class="f-h" style="left:85px">LUMENGRID THEME</div>
<p class="abs f-txt" style="left:85px;top:1806px;width:245px">Ipsum is simply dummy text<br>of the printing and typesetting industry.Ip-<br>sum is simply<br>More Info</p>

<div class="f-h" style="left:346px">RECENT POSTS W/THUMB</div>
<div class="post" style="top:1817px"><div class="th" role="img" aria-label="Coral thumbnail"></div><div class="t">The cutest umbrella ever!</div><div class="x">He lay on his armour-like back, and ...</div></div>
<div class="post" style="top:1908px"><div class="th" style="background:linear-gradient(135deg,#c46a2a,#3f7a8a)" role="img" aria-label="Clownfish thumbnail"></div><div class="t">Pretty females gallery format</div><div class="x">Nam quam nunc, blandit vel, luctus pulvinar, ...</div></div>
<div class="post" style="top:1999px"><div class="th" role="img" aria-label="Coral thumbnail"></div><div class="t">Live strong..or high?</div><div class="x">No one rejects, dislikes, or avoids pleasure ...</div></div>

<div class="f-h" style="left:608px">TAG CLOUD</div>
<div class="tags"><span>animals</span><span>audio</span><span>blonde</span><span>cars</span><span>children</span><span>doggy</span><span>famous quotes</span><span>gallery format</span><span>kids</span><span>models</span><span>photos</span><span>Post formats</span><span>Quote</span><span>standard post</span><span>Travel</span><span>Video format</span><span>clipora</span></div>

<div class="f-h" style="left:870px">RECENTLY ADDED</div>
<div class="recent" style="top:1815px"><div class="t">The cutest umbrella ever!</div><div class="d">February 10, 2014</div></div>
<div class="recent" style="top:1870px"><div class="t">Pretty females gallery format</div><div class="d">January 21, 2014</div></div>
<div class="recent" style="top:1925px"><div class="t">Live strong..or high?</div><div class="d">January 20, 2014</div></div>
<div class="recent" style="top:1980px;border:0"><div class="t">A quote from Edmund Varley</div><div class="d">January 20, 2014</div></div>

<div class="abs footer-bar"></div>
<div class="abs copy">© 2014scuba diving center All Rights Reserved</div>
<div class="social" aria-label="Social links">
  <span style="background:#c8232c"></span><span style="background:#3f729b"></span><span style="background:#dd4b39"></span><span style="background:#0077b5"></span><span style="background:#ea4c89"></span><span style="background:#3a5a98"></span><span style="background:#1da1f2"></span><span style="background:#0b86ca"></span><span style="background:#3cbc3c"></span><span style="background:#3b5998"></span><span style="background:#e8761c"></span>
</div>

</body>
</html>
```